Business card design reauest

2 sided. White on both sides

Gordon Mabry

Ho Chi Minh, Vietnam

Cell Phone / Whatsapp/ Wechat/Zalo
1-555-382-7194
Gmabry@kwpartsworks.vn
Www.kwpartsworks.vn
Www.kwpartsworks.com

Industry/Entity Type

Sofa and furniture and kitchen

Contact Information for Business Card

2 sided. White on both sides Gordon Mabry Ho Chi Minh, Vietnam Cell Phone / Whatsapp/ Wechat/Zalo 1-555-382-7194 Gmabry@kwpartsworks.vn Www.kwpartsworks.vn Www.kwpartsworks.com

```html
<!DOCTYPE html>
<html lang="en">
<head>
<meta charset="utf-8">
<title>KW Parts Works – Business Card</title>
<link rel="stylesheet" href="https://fonts.googleapis.com/css2?family=Crimson+Pro:wght@400;600;700&display=swap">
<style>
  :root {
    --backdrop: #e9e7e3;
    --card: #ffffff;
    --brand-green: #0f9a3a;
    --ink: #231f20;
    --shadow: rgba(0, 0, 0, 0.18);
  }
  * { margin: 0; padding: 0; box-sizing: border-box; }
  html, body {
    width: 1181px;
    height: 1200px;
    overflow: hidden;
    background: var(--backdrop);
    font-family: "Crimson Pro", Georgia, serif;
    color: var(--ink);
  }
  .canvas { position: relative; width: 1181px; height: 1200px; }
  .card {
    position: absolute;
    background: var(--card);
    box-shadow: 0 8px 22px var(--shadow);
  }
  .card--front { left: 219px; top: 128px; width: 747px; height: 427px; }
  .card--back  { left: 223px; top: 655px; width: 737px; height: 422px; }

  .front__brand {
    position: absolute;
    left: 40px; top: 220px; width: 240px;
    text-align: center;
    color: var(--brand-green);
    font-weight: 600;
    font-size: 26px;
    letter-spacing: 0.5px;
  }
  .front__divider {
    position: absolute;
    left: 327px; top: 60px;
    width: 1.5px; height: 307px;
    background: var(--ink);
  }
  .contact { position: absolute; left: 374px; top: 92px; }
  .contact__name {
    color: var(--brand-green);
    font-weight: 700;
    font-size: 42px;
    line-height: 1;
    letter-spacing: 0.3px;
  }
  .contact__location {
    margin-top: 4px;
    font-weight: 600;
    font-size: 19px;
    letter-spacing: 0.2px;
  }
  .contact__list { list-style: none; margin-top: 38px; }
  .contact__item {
    display: flex;
    align-items: center;
    height: 42px;
    font-size: 23px;
  }
  .contact__icon { width: 27px; height: 27px; margin-right: 19px; flex: none; }

  .back__brand {
    position: absolute;
    left: 0; right: 0; top: 150px;
    text-align: center;
    color: var(--brand-green);
    font-weight: 600;
    font-size: 52px;
    letter-spacing: 1px;
  }
  .back__web {
    position: absolute;
    left: 0; right: 0; top: 352px;
    text-align: center;
    font-weight: 700;
    font-size: 24px;
    letter-spacing: 7px;
  }
</style>
</head>
<body>
<main class="canvas">
  <section class="card card--front">
    <div class="front__brand">KW PARTS WORKS</div>
    <div class="front__divider"></div>
    <div class="contact">
      <h1 class="contact__name">Gordon Mabry</h1>
      <p class="contact__location">HO CHI MINH, VIETNAM</p>
      <ul class="contact__list">
        <li class="contact__item">
          <svg class="contact__icon" viewBox="0 0 28 28" aria-hidden="true">
            <circle cx="14" cy="14" r="14" fill="var(--brand-green)"/>
            <path d="M9 7.5c1-.8 2-.6 2.6.3l1.3 2.1c.5.8.3 1.6-.4 2.1l-.9.6c.6 1.6 1.9 3 3.5 3.6l.6-.9c.5-.7 1.3-.9 2.1-.4l2.1 1.3c.9.6 1.1 1.6.3 2.6-1.3 1.6-3.3 1.9-5.6.6-2.8-1.6-4.8-3.9-5.8-6.6-.7-2-.4-3.8.2-5.3z" fill="#fff"/>
          </svg>
          (555) 382-7194
        </li>
        <li class="contact__item">
          <svg class="contact__icon" viewBox="0 0 28 28" aria-hidden="true">
            <circle cx="14" cy="14" r="14" fill="var(--brand-green)"/>
            <rect x="7.5" y="9.5" width="13" height="9" fill="#fff"/>
            <path d="M7.5 9.5l6.5 5 6.5-5M7.5 18.5l4.6-4.2M20.5 18.5l-4.6-4.2" fill="none" stroke="var(--brand-green)" stroke-width="0.9"/>
          </svg>
          Gmabry@kwpartsworks.vn
        </li>
        <li class="contact__item">
          <svg class="contact__icon" viewBox="0 0 28 28" aria-hidden="true">
            <circle cx="14" cy="14" r="14" fill="var(--brand-green)"/>
            <g fill="none" stroke="#fff" stroke-width="1.4">
              <circle cx="14" cy="14" r="8.5"/>
              <ellipse cx="14" cy="14" rx="3.8" ry="8.5"/>
              <path d="M5.5 14h17M7 9.5h14M7 18.5h14"/>
            </g>
          </svg>
          Www.kwpartsworks.vn
        </li>
      </ul>
    </div>
  </section>

  <section class="card card--back">
    <div class="back__brand">KW PARTS WORKS</div>
    <p class="back__web">Www.kwpartsworks.com</p>
  </section>
</main>
</body>
</html>
```